Farhan Dalvesi Business Card

I would like an elegant business card design in both english and arabic.

Ideally a logo design with my name in Arabic (could be a tiger for example)

It should have my Name : Farhan Dalvesi
Title: Advisor / Investor
Tel. UAE +971 558 402 917
UK +44 7812 506 284
Email. farhdalv352@mailvora.com

I am an active angle investor and have many business interests in the TMT space and invest globally, the design needs to be fresh, elegant and striking.

The design should be catching and grab one's attention when they view the card.

Front card should be in English and Reverse in Arabic....

Target Market(s)

Global Investors, CEO's

Industry/Entity Type

Business

Contact Information for Business Card

Title: Advisor / Investor
Tel. UAE +971 558 402 917
UK +44 7812 506 284

Font styles to use
Serif
Other font styles liked:
• Palantino

Requirements
Must have
• A striking design with a play of my name in Arabic, could be my name that is designed as a tiger for example

```html
<!DOCTYPE html>
<html lang="en">
<head>
<meta charset="utf-8">
<title>Farhan Dalvesi Business Card</title>
<link rel="stylesheet" href="https://fonts.googleapis.com/css2?family=Arvo:wght@400;700&family=Noto+Naskh+Arabic:wght@400&display=swap">
<style>
  :root {
    --page: #e6e4e0;
    --paper: #ffffff;
    --saffron: #f9b51a;
    --ink: #1c1c1c;
    --maroon: #8b1a12;
    --edge: #d2d0cc;
  }
  * { box-sizing: border-box; margin: 0; padding: 0; }
  html, body { width: 1200px; height: 1000px; overflow: hidden; }
  body {
    background: var(--page);
    font-family: "Arvo", Georgia, serif;
    color: var(--ink);
    position: relative;
  }
  .card {
    position: absolute;
    left: 220px;
    width: 760px;
    height: 434px;
    background: var(--paper);
    box-shadow: 0 2px 0 var(--edge), 0 10px 24px rgba(0,0,0,.12);
    overflow: hidden;
  }
  .card--front { top: 40px; }
  .card--back { top: 526px; }
  .card__art { position: absolute; inset: 0; width: 100%; height: 100%; }

  /* Front */
  .identity { position: absolute; left: 70px; top: 130px; }
  .identity__mark { display: flex; align-items: center; gap: 14px; }
  .identity__first { font-size: 64px; line-height: 1; color: var(--ink); }
  .identity__dot { width: 30px; height: 30px; border-radius: 50%; background: var(--maroon); }
  .identity__last { font-size: 38px; line-height: 1.1; margin-top: 10px; }
  .identity__title { font-size: 15px; letter-spacing: .04em; margin-top: 6px; }

  .contact {
    position: absolute;
    left: 520px; top: 36px; width: 210px;
    text-align: center;
    font-size: 15px;
    line-height: 1.45;
    color: var(--ink);
  }
  .contact__icon { display: block; margin: 0 auto 10px; }
  .contact__group { margin-bottom: 34px; }
  .contact__email { font-size: 13px; }

  /* Back (Arabic reverse) */
  .back-mark {
    position: absolute; left: 330px; top: 70px;
    display: flex; align-items: center; gap: 14px;
  }
  .back-mark__name {
    font-family: "Noto Naskh Arabic", "Arvo", serif;
    font-size: 56px; line-height: 1.2; color: var(--ink);
  }
  .back-mark__dot { width: 24px; height: 24px; border-radius: 50%; background: var(--maroon); }
  .statement {
    position: absolute; left: 60px; top: 282px; width: 650px;
    font-size: 16px; line-height: 1.5; color: var(--ink);
  }
  .statement__web {
    font-size: 24px; margin-top: 12px; color: var(--maroon);
    text-align: right; padding-right: 60px;
  }
</style>
</head>
<body>

<section class="card card--front" aria-label="Card front">
  <svg class="card__art" viewBox="0 0 760 434" aria-hidden="true">
    <path d="M440 0 C425 80 470 150 500 230 C530 310 540 380 560 434 L760 434 L760 0 Z" fill="var(--saffron)"/>
    <path d="M436 0 C420 82 466 152 496 232 C526 312 536 382 556 434" fill="none" stroke="var(--ink)" stroke-width="2"/>
    <path d="M446 0 C428 76 476 146 506 226 C534 306 546 378 566 434" fill="none" stroke="var(--ink)" stroke-width="1.4"/>
  </svg>

  <div class="identity">
    <div class="identity__mark">
      <span class="identity__first">Farhan</span>
      <span class="identity__dot"></span>
    </div>
    <div class="identity__last">Dalvesi</div>
    <div class="identity__title">Advisor / Investor</div>
  </div>

  <div class="contact">
    <div class="contact__group">
      <svg class="contact__icon" width="26" height="26" viewBox="0 0 24 24" aria-hidden="true">
        <path fill="#fff" d="M6.6 10.8a15.1 15.1 0 0 0 6.6 6.6l2.2-2.2a1 1 0 0 1 1-.25 11.4 11.4 0 0 0 3.6.57 1 1 0 0 1 1 1V20a1 1 0 0 1-1 1A17 17 0 0 1 3 4a1 1 0 0 1 1-1h3.5a1 1 0 0 1 1 1c0 1.25.2 2.45.57 3.6a1 1 0 0 1-.25 1z"/>
      </svg>
      <div>UAE +971 558 402 917</div>
      <div>UK +44 7812 506 284</div>
    </div>
    <div class="contact__group">
      <svg class="contact__icon" width="26" height="18" viewBox="0 0 26 18" aria-hidden="true">
        <rect x="0.5" y="0.5" width="25" height="17" fill="#fff"/>
        <path d="M1 1 L13 10 L25 1" fill="none" stroke="var(--saffron)" stroke-width="1.5"/>
      </svg>
      <div class="contact__email">farhdalv352@mailvora.com</div>
    </div>
    <div class="contact__group">
      <svg class="contact__icon" width="24" height="24" viewBox="0 0 24 24" aria-hidden="true">
        <circle cx="12" cy="12" r="10" fill="none" stroke="#fff" stroke-width="1.6"/>
        <ellipse cx="12" cy="12" rx="4.5" ry="10" fill="none" stroke="#fff" stroke-width="1.4"/>
        <path d="M2 12 H22 M4 7 H20 M4 17 H20" stroke="#fff" stroke-width="1.2"/>
      </svg>
      <div>www.farhandalvesi.com</div>
    </div>
  </div>
</section>

<section class="card card--back" aria-label="Card back">
  <svg class="card__art" viewBox="0 0 760 434" aria-hidden="true">
    <path d="M0 250 C150 220 260 196 420 200 C560 204 640 120 760 80 L760 434 L0 434 Z" fill="var(--saffron)"/>
    <path d="M0 246 C150 216 262 192 420 196 C560 200 640 116 760 76" fill="none" stroke="var(--ink)" stroke-width="2"/>
    <path d="M0 256 C160 222 250 204 418 206 C566 210 634 130 760 88" fill="none" stroke="var(--ink)" stroke-width="1.4"/>
  </svg>

  <div class="back-mark">
    <span class="back-mark__name" lang="ar" dir="rtl">فرحان</span>
    <span class="back-mark__dot"></span>
  </div>

  <div class="statement">
    <p>Lorem ipsum dolor sit amet, consectetur adipiscing elit, sed do eiusmod tempor incididunt ut labore et dolore magna aliqua. Ut enim ad minim veniam, quis nostrud exercitation ullamco laboris.</p>
    <p class="statement__web">www.farhandalvesi.com</p>
  </div>
</section>

</body>
</html>
```